Letterhead for clinic notes, test reports, and business cards

I need business card and letterheads for a medical clinic with the following:
1- Business cards. The back should allow for space for date and time of next appointments (few lines would do)
2- Letterhead for clinic notes
3- Letterhead for test reports.

Feel free to use whats included for examples. I value creativity so be creative.

Target Market(s)

Patients, referring physicians.

Industry/Entity Type

Health Care

Requirements
Must have
• Must use current logo.
• Must look good on white background
• Letterhead and reports must look good faxed.
• Please use themes of the current logo. Another possible color to use is grey as well (www.brambleveincare.org - use the font color in the text of that website)

```html
<!DOCTYPE html>
<html lang="en">
<head>
<meta charset="utf-8">
<title>Kestrel Heart Institute – Letterhead Set</title>
<link rel="stylesheet" href="https://fonts.googleapis.com/css2?family=Questrial&display=swap">
<style>
  :root {
    --page: #fcfcf9;
    --ink: #1b1b1b;
    --brand-blue: #1a3d9c;
    --footer-red: #7a0a05;
    --rule-blue: #1c3a97;
    --canvas: #ffffff;
  }
  * { box-sizing: border-box; margin: 0; padding: 0; }
  html, body { width: 1200px; height: 1200px; overflow: hidden; background: var(--canvas); }
  body { position: relative; font-family: "Questrial", sans-serif; color: var(--ink); }

  .sheet {
    position: absolute;
    width: 594px; height: 768px;
    background: var(--page);
    box-shadow: 0 0 10px rgba(0,0,0,0.28);
    overflow: hidden;
  }
  .sheet--report { left: 76px; top: 68px; }
  .sheet--letter { left: 541px; top: 374px; }

  .brand {
    position: absolute; right: 16px; top: 62px;
    text-align: center; color: var(--brand-blue);
    font-size: 19px; line-height: 1; letter-spacing: 0.02em;
  }
  .brand__sub { display: block; font-size: 12px; letter-spacing: 0.08em; margin-top: 3px; }

  .field, .line {
    position: absolute; left: 18px;
    font-size: 11px; letter-spacing: 0.09em; white-space: nowrap; line-height: 14px;
  }
  .field__value { position: absolute; left: 66px; top: 0; }

  .report-table {
    position: absolute; left: 18px; top: 186px;
    width: 561px; height: 211px;
    border-collapse: collapse;
  }
  .report-table td { border: 1px solid #222; height: 16.2px; }

  .rule { position: absolute; left: 0; right: 0; top: 702px; height: 4px; background: var(--rule-blue); }
  .footer {
    position: absolute; left: 0; right: 0; top: 710px; height: 58px;
    background: var(--footer-red); color: #fff;
    text-align: center; font-size: 10.5px; letter-spacing: 0.08em; line-height: 13px;
    padding-top: 18px; white-space: nowrap;
  }
</style>
</head>
<body>

<section class="sheet sheet--report" aria-label="Test report letterhead">
  <div class="brand">KESTREL HEART<span class="brand__sub">INSTITUTE</span></div>
  <p class="field" style="top:116px">Date: MM.DD.YYYY</p>
  <p class="field" style="top:144px">Address:<span class="field__value">1187 Larkspur Avenue Suite 304<br>Halden, Ontario K4R2P9</span></p>
  <table class="report-table">
    <colgroup><col style="width:131px"><col style="width:97px"><col style="width:191px"><col></colgroup>
    <tbody>
      <tr><td></td><td></td><td></td><td></td></tr>
      <tr><td></td><td></td><td></td><td></td></tr>
      <tr><td></td><td></td><td></td><td></td></tr>
      <tr><td></td><td></td><td></td><td></td></tr>
      <tr><td></td><td></td><td></td><td></td></tr>
      <tr><td></td><td></td><td></td><td></td></tr>
      <tr><td></td><td></td><td></td><td></td></tr>
      <tr><td></td><td></td><td></td><td></td></tr>
      <tr><td></td><td></td><td></td><td></td></tr>
      <tr><td></td><td></td><td></td><td></td></tr>
      <tr><td></td><td></td><td></td><td></td></tr>
      <tr><td></td><td></td><td></td><td></td></tr>
      <tr><td></td><td></td><td></td><td></td></tr>
    </tbody>
  </table>
  <div class="rule"></div>
  <footer class="footer">1187 LARKSPUR AVENUE SUITE 304 HALDEN, ON K4R2P9 &nbsp;|&nbsp; PHONE: 555.014.2290<br>FAX: 555.014.2291 &nbsp;|&nbsp; EMAIL: CONTACT@KESTRELHEART.ORG</footer>
</section>

<section class="sheet sheet--letter" aria-label="Clinic notes letterhead">
  <div class="brand">KESTREL HEART<span class="brand__sub">INSTITUTE</span></div>
  <p class="field" style="top:116px">Date: MM.DD.YYYY</p>
  <p class="field" style="top:144px">Address:<span class="field__value">1187 Larkspur Avenue Suite 304<br>Halden, Ontario K4R2P9</span></p>
  <p class="line" style="top:186px">Salutation,</p>
  <p class="line" style="top:214px">Lorem ipsum dolor sit amet, tota dolor rationibus ea vis, vix partem doming tacimates ea.</p>
  <p class="line" style="top:228px">Nisl decore vituperatoribus ius ad. Ex nulla iuvaret his, reprimique deterruisset cum no.</p>
  <p class="line" style="top:242px">Sea dicat minimum fierent id. Cetero deleniti scribentur ius ex. Sea congue expetendis</p>
  <p class="line" style="top:256px">reprimique an.</p>
  <p class="line" style="top:284px">Lorem vocent ad qui, fabulas epicurei pro no, in meis democritum pri. Qui scripta electram</p>
  <p class="line" style="top:298px">ex. Facer mundi nam ne. Pro agam prompta te. Esse modus in vel, per et periculis percipi-</p>
  <p class="line" style="top:312px">tur, per eu nobis saperet.</p>
  <p class="line" style="top:340px">Complementary Close,</p>
  <p class="line" style="top:368px">Signature</p>
  <p class="line" style="top:382px">Name of Sender</p>
  <p class="line" style="top:396px">Title</p>
  <p class="line" style="top:424px">CC/cc</p>
  <div class="rule"></div>
  <footer class="footer">1187 LARKSPUR AVENUE SUITE 304 HALDEN, ON K4R2P9 &nbsp;|&nbsp; PHONE: 555.014.2290<br>FAX: 555.014.2291 &nbsp;|&nbsp; EMAIL: CONTACT@KESTRELHEART.ORG</footer>
</section>

</body>
</html>
```